依頼詳細
開業して1年を迎えたので、新たなチラシ作成をお願いしたいと思っております。
新聞折込とポスティングを行います。
記載項目
ロゴマーク
松風7丁目鍼灸マッサージ院
休診日 月曜日
受付時間 火・水・木 9:00~19:00 金・土 9:00~20:00 日 9:00~18:00
〒318-0761
東京都葛飾区松風7丁目3-28 シエルコート205
090-4312-5968

想い
松風7丁目鍼灸マッサージ院です。 地域密着を目指し、 一人でも多くの人が、いくつになっても自分の足で 健康的に元気に歩いている社会になってもらいたい。 健康寿命が長い街、地域になってほしい、 その想いから、その人、一人ひとりにあったプランを考えて、施術を行っていきます。 今後の高齢化社会に向けて、みなさまの、悪くならない、 痛くならない体づくりのお手伝いができたらと思います。

ミントリーフスタイルのQRコード
予約サイトPelvora(ペルヴォラ)のQRコード
サイズ
A4
ページ数
片面
希望イメージ
シンプル 複雑
単色 カラフル
暗い 明るい
日常 高級
遊び心 厳粛
未来的 伝統的
女性的 男性的
希望する色
赤系、黄・オレンジ系、緑系
納品ファイル
補足説明
今まで配っていたチラシも添付しておきます。
ご参考になれば幸いです。

落ち着きがあり、明るくかわいい感じで仕上げていただきました。
温かみもありホッとする感じがしました。
お願いした色合いとは異なりましたが、一目見て、すぐに、候補の一つに上がりました。
本当にありがとうございます。

今回は当院のチラシデザインの制作コンペに参加いただき、ありがとうございます。
以前お願いしていたデザイナーさんと連絡が取れなくなり、大変困っていました。
そんな中、初めてテンポリカを使ってみました。
最初は「本当に応募なんか来るのか?」「気に入る作品は提案されるのか?」とても不安でした。
ふたを開けてみたら、提案はたくさん来るし、どれも素晴らしい提案だしで、良い意味で困りました。
今回は、本当に、多数のご提案、ありがとうございました。

また来年お願いするかもしれません。
その時はまた、よろしくお願いします。

```html
<!DOCTYPE html>
<html lang="ja">
<head>
<meta charset="utf-8">
<title>松風7丁目鍼灸マッサージ院 チラシ</title>
<link rel="stylesheet" href="https://fonts.googleapis.com/css2?family=M+PLUS+Rounded+1c:wght@500;700;800&family=Zen+Maru+Gothic:wght@500;700;900&display=swap">
<style>
:root{
  --coral:#e98a72;
  --coral-deep:#dc735b;
  --coral-soft:#f3b5a3;
  --blush:#f7d5c9;
  --cream:#fff8f2;
  --brown:#7a5a4a;
  --ink:#5b4035;
  --white:#ffffff;
  --sage:#c9d3b8;
}
*{margin:0;padding:0;box-sizing:border-box}
html,body{width:846px;height:1200px;overflow:hidden;background:var(--white)}
body{font-family:"Zen Maru Gothic","M PLUS Rounded 1c",sans-serif;color:var(--ink)}
.flyer{position:relative;width:846px;height:1200px;overflow:hidden;background:var(--white)}
.abs{position:absolute}
.front{z-index:3}

/* header */
.brand{left:28px;top:22px;display:flex;align-items:center;gap:14px}
.brand-mark{width:66px;height:66px;border-radius:50%;background:var(--coral);flex:none}
.brand-name{font-weight:700;font-size:27px;line-height:1.2;color:var(--brown)}
.anniversary{left:452px;top:18px;width:394px;height:64px;background:var(--coral);
  color:var(--white);font-weight:700;font-size:17px;line-height:1.45;padding:8px 0 0 20px;
  border-radius:32px 0 0 32px}

/* main coral field */
.field{left:0;top:112px;width:846px;height:818px;background:var(--coral)}
.blob{border-radius:50%;background:var(--coral-deep);opacity:.35}
.lead{left:40px;top:136px;color:var(--white);font-weight:700;font-size:29px;letter-spacing:1px}
.headline{left:36px;top:180px;color:var(--white);font-weight:900;font-size:41px;letter-spacing:1px;white-space:nowrap}
.symptoms{left:44px;top:254px;width:440px;display:grid;grid-template-columns:repeat(4,1fr);gap:8px;list-style:none}
.symptom{background:var(--white);color:var(--coral-deep);font-weight:700;font-size:17px;text-align:center;padding:6px 0;border-radius:3px}
.symptoms-note{left:44px;top:346px;width:440px;text-align:center;color:var(--white);font-weight:700;font-size:19px}

.scene{border-radius:50%;border:8px solid var(--white);overflow:hidden}
.scene-walk{left:560px;top:140px;width:270px;height:270px;background:radial-gradient(circle at 60% 60%,var(--sage),var(--cream))}
.scene-couple{left:-30px;top:400px;width:330px;height:330px;background:radial-gradient(circle at 50% 60%,var(--blush),var(--cream))}
.scene-family{left:470px;top:610px;width:330px;height:330px;background:radial-gradient(circle at 50% 60%,var(--blush),var(--cream))}
.scene-caption{color:var(--brown);font-weight:700;font-size:19px;line-height:1.35;text-align:center}

.hero-band{left:250px;top:466px;width:596px;height:140px;background:var(--white);border-radius:70px 0 0 70px}
.hero-title{left:300px;top:470px;color:var(--coral-deep);font-family:"M PLUS Rounded 1c",sans-serif;font-weight:800;font-size:76px;letter-spacing:2px}
.hero-title small{font-size:44px}
.hero-sub{left:318px;top:560px;color:var(--brown);font-weight:900;font-size:34px;letter-spacing:1px}

.message{left:40px;top:748px;width:420px;color:var(--white);font-weight:500;font-size:15.5px;line-height:1.75}

/* footer */
.footer-brand{left:60px;top:948px;display:flex;align-items:center;gap:12px}
.footer-brand .brand-mark{width:44px;height:44px}
.footer-brand .brand-name{font-size:24px}
.access-label{left:18px;top:1000px;width:28px;height:120px;background:var(--coral);color:var(--white);
  font-weight:700;font-size:15px;writing-mode:vertical-rl;text-align:center;line-height:28px;letter-spacing:4px}
.info{left:60px;top:1004px;font-size:12.5px;line-height:1.75;color:var(--ink);font-weight:500}
.info b{color:var(--coral-deep);font-weight:700;margin-right:6px}
.phone{left:56px;top:1096px;display:flex;align-items:center;gap:8px;color:var(--coral-deep);font-weight:900;font-size:34px;letter-spacing:1px}
.director{left:60px;top:1160px;font-size:12px;color:var(--brown)}

.partner{top:1062px;width:120px;display:flex;flex-direction:column;align-items:center;gap:5px;font-size:11px;font-weight:700;color:var(--brown);white-space:nowrap}
.qr{width:56px;height:56px;background:var(--ink);border-radius:3px}
.partner-mint{left:340px}
.partner-pelvora{left:466px}

.map{left:600px;top:940px;width:232px;height:180px;background:linear-gradient(135deg,var(--cream),var(--blush));border-radius:6px}
</style>
</head>
<body>
<div class="flyer">

  <header>
    <div class="abs brand">
      <span class="brand-mark"></span>
      <div class="brand-name">松風7丁目<br>鍼灸マッサージ院</div>
    </div>
    <p class="abs anniversary">おかげさまで開業して1年を迎えました!<br>どうもありがとうございます!</p>
  </header>

  <main>
    <div class="abs field"></div>
    <div class="abs blob" style="left:420px;top:300px;width:360px;height:260px"></div>
    <div class="abs blob" style="left:-60px;top:800px;width:300px;height:130px;border-radius:150px 150px 0 0"></div>

    <div class="abs scene scene-walk" role="img" aria-label="犬と散歩する女性のイラスト"></div>
    <p class="abs scene-caption" style="left:640px;top:172px">痛みのない<br>身体で<br>快適な生活を</p>

    <p class="abs lead front">あなたのその慢性化した症状</p>
    <h1 class="abs headline front">鍼灸で悩みが解決できます</h1>

    <ul class="abs symptoms front">
      <li class="symptom">腰痛</li><li class="symptom">肩こり</li><li class="symptom">足の痛み</li><li class="symptom">めまい</li>
      <li class="symptom">耳鳴り</li><li class="symptom">眼精疲労</li><li class="symptom">冷え性</li><li class="symptom">不眠</li>
    </ul>
    <p class="abs symptoms-note">様々な身体の不調</p>

    <div class="abs scene scene-couple" role="img" aria-label="寄り添って歩く高齢の夫婦のイラスト"></div>
    <p class="abs scene-caption" style="left:130px;top:430px">若い頃のような<br>身体を取り戻す</p>

    <div class="abs hero-band"></div>
    <h2 class="abs hero-title">快癒<small>へ導く</small></h2>
    <p class="abs hero-sub">地域密着のマッサージ院</p>

    <div class="abs scene scene-family" role="img" aria-label="手をつないで歩く家族のイラスト"></div>
    <p class="abs scene-caption" style="left:600px;top:640px">疲れない<br>身体で<br>人生を楽しむ</p>

    <p class="abs message">鍼灸が得意とするのは「痛み、こり・しびれ・不調」です。慢性化していつも身体の調子が悪いという方はまずは一度ご相談ください。しっかりとカウンセリングを行い、経験豊富なスタッフがあなたの体の調整やお悩みをじっくりとお聞きします。</p>
  </main>

  <footer>
    <div class="abs footer-brand">
      <span class="brand-mark"></span>
      <div class="brand-name">松風7丁目鍼灸マッサージ院</div>
    </div>
    <div class="abs access-label">アクセス</div>
    <p class="abs info">〒318-0761 東京都葛飾区松風7丁目3-28 シエルコート205<br>
      <b>受付時間</b>火・水・木 9:00~19:00 / 金・土 9:00~20:00 / 日 9:00~18:00<br>
      <b>休診日</b>月曜日</p>
    <div class="abs phone">
      <svg width="28" height="28" viewBox="0 0 24 24" aria-hidden="true"><path fill="#dc735b" d="M6.6 10.8a15.1 15.1 0 0 0 6.6 6.6l2.2-2.2a1 1 0 0 1 1-.25 11.4 11.4 0 0 0 3.6.57 1 1 0 0 1 1 1V20a1 1 0 0 1-1 1A17 17 0 0 1 3 4a1 1 0 0 1 1-1h3.5a1 1 0 0 1 1 1c0 1.25.2 2.45.57 3.57a1 1 0 0 1-.25 1z"/></svg>
      090-4312-5968
    </div>
    <p class="abs director">院長 森野 孝介</p>

    <div class="abs partner partner-mint"><span class="qr"></span>ミントリーフスタイル</div>
    <div class="abs partner partner-pelvora"><span class="qr"></span>予約サイト Pelvora</div>

    <div class="abs map" role="img" aria-label="駅から院までの周辺地図"></div>
  </footer>

</div>
</body>
</html>
```